Daniel Horvath Photography Business Card

I am a photographer in Philadelphia, PA. I have a business card that I have designed in Photoshop. This has been an ongoing process for me for far too long. I am 85% pleased with what I have. I need some experts like yourself who has that extra 25% to make this card 110%. I use the dots throughout my website as page/topic breaks. I also use the dots on the mailing side of my direct mail pieces.

Bluefield Printworks does my printing.
Their File Specs for a business card:
width - 3.625 inches
Height - 2.124 inches
@ 355 PPI or DPI
CMYK
1/8 inch Bleed/CUT
This is the size of my uploaded file samples

I will have the card printed on a 18 pt card stock - 4 color - 2 sides - with a matte coating

Tech Info: SIDE 01
For name DANIEL HORVATH : font choice is FoglihtenNo07 - size 14.4 - VA 150 - Text Height 140% - text width 130% - underlined - color is 30 - 30- 30 or (1e1e1e)
For word PHOTOGRAPHY : font choice is FoglihtenNo07 - size 6.4 - VA 360 - Text Height 200% - text width 270% - underlined - color is 162-162-162 or (a2a2a2)
For DOTS - font choice is FoglihtenNo07 - size 6.73 - VA 180 - Text Height 100% - text width 163% - color is 100-179-204 or (64b3cc) - blue dots / 1-1-1 or (010101) - Black dots
For DAN@DHORVATHSTUDIO.EXAMPLE - font choice is Helvetica Neue Light - size 4.55 - VA 121 - Text Height 200% - text width 132% - color is 1-1-1 or (010101)
For 555.418.7260 - font choice is Helvetica Neue Light - size 4.55 - VA 270 - Text Height 180% - text width 189% - color is 1-1-1 or (010101)
For DHORVATHSTUDIO.EXAMPLE - font choice is Helvetica Neue Light - size 9.1 - VA 180 - Text Height 150% - text width 130% - color is 133-192-214 or (85c0d6)

Tech Info: SIDE 02
not certain if it is my website address - DHORVATHSTUDIO.EXAMPLE - like the sample or
or my Logo with dots DANIEL HORVATH PHOTOGRAPHY, WITH UNDERLINEs AND DOTS JUST LIKE FIRST SIDE - MAYBE BIGGER
the name in Helvetica Neue Light - 255 pure white -
Dots are same colors as first side
The background color of choice - at least for now issssss: 84-91-99 or (545b63)

If you think you can make my card really say Wow! Please let me know. Thank you very much!

Target Market(s)

Ad Agencies

Industry/Entity Type

Professional Photography

Contact Information for Business Card

width - 3.625 inches
Height - 2.124 inches
@ 355 PPI or DPI
CMYK
1/8 inch Bleed/CUT

Tech Info: SIDE 01

Tech Info: SIDE 02

Font styles to use
Other font styles liked:
• FoglihtenNo07 and Helvetica Neue Light

Requirements
Must have
• I am a photographer in Philadelphia, PA. I have a business card that I have designed in Photoshop. This has been an ongoing process for me for far too long. I am 85% pleased with what I have. I need some experts like yourself who has that extra 25% to make this card 110%. I use the dots throughout my website as page/topic breaks. I also use the dots on the mailing side of my direct mail pieces.
• Bluefield Printworks does my printing.
• Their File Specs for a business card:
• width - 3.625 inches
• Height - 2.124 inches
• @ 355 PPI or DPI
• CMYK
• 1/8 inch Bleed/CUT
• This is the size of my uploaded file samples
• I will have the card printed on a 18 pt card stock - 4 color - 2 sides - with a matte coating
• Tech Info: SIDE 01
• For name DANIEL HORVATH : font choice is FoglihtenNo07 - size 14.4 - VA 150 - Text Height 140% - text width 130% - underlined - color is 30 - 30- 30 or (1e1e1e)
• For word PHOTOGRAPHY : font choice is FoglihtenNo07 - size 6.4 - VA 360 - Text Height 200% - text width 270% - underlined - color is 162-162-162 or (a2a2a2)
• For DOTS - font choice is FoglihtenNo07 - size 6.73 - VA 180 - Text Height 100% - text width 163% - color is 100-179-204 or (64b3cc) - blue dots / 1-1-1 or (010101) - Black dots
• For DAN@DHORVATHSTUDIO.EXAMPLE - font choice is Helvetica Neue Light - size 4.55 - VA 121 - Text Height 200% - text width 132% - color is 1-1-1 or (010101)
• For 555.418.7260 - font choice is Helvetica Neue Light - size 4.55 - VA 270 - Text Height 180% - text width 189% - color is 1-1-1 or (010101)
• For DHORVATHSTUDIO.EXAMPLE - font choice is Helvetica Neue Light - size 9.1 - VA 180 - Text Height 150% - text width 130% - color is 133-192-214 or (85c0d6)
• Tech Info: SIDE 02
• not certain if it is my website address - DHORVATHSTUDIO.EXAMPLE - like the sample or
• or my Logo with dots DANIEL HORVATH PHOTOGRAPHY, WITH UNDERLINEs AND DOTS JUST LIKE FIRST SIDE - MAYBE BIGGER
• the name in Helvetica Neue Light - 255 pure white -
• Dots are same colors as first side
• The background color of choice - at least for now issssss: 84-91-99 or (545b63)
• If you think you can make my card really say Wow! Please let me know. Thank you very much!
Nice to have
• I could really use some different sizes of the dots as a Vector file?? I use Photoshop for all my designs. Thank You.
Should not have
• all listed above

```html
<!DOCTYPE html>
<html lang="en">
<head>
<meta charset="utf-8">
<title>Daniel Horvath Photography – Business Card</title>
<link rel="stylesheet" href="https://fonts.googleapis.com/css2?family=Roboto:wght@300&display=swap">
<style>
  :root {
    --card-dark: #121416;
    --card-mid: #1b1e21;
    --accent-teal: #80d8d9;
    --text-white: #ffffff;
    --dot-white: #ffffff;
  }
  html, body {
    margin: 0;
    padding: 0;
    width: 1200px;
    height: 686px;
    overflow: hidden;
    background: var(--card-dark);
  }
  .card {
    position: relative;
    width: 1200px;
    height: 686px;
    overflow: hidden;
    font-family: "Roboto", "Helvetica Neue", Arial, sans-serif;
    font-weight: 300;
    color: var(--text-white);
  }
  .card-texture {
    position: absolute;
    inset: 0;
    background: radial-gradient(ellipse at 50% 45%, var(--card-mid) 0%, var(--card-dark) 75%);
  }
  .pill {
    position: absolute;
    box-sizing: border-box;
    border: 2.5px solid var(--accent-teal);
    border-radius: 18px;
    display: flex;
    align-items: center;
    justify-content: center;
    white-space: nowrap;
    line-height: 1;
  }
  .website {
    left: 178px;
    top: 213px;
    width: 844px;
    height: 83px;
    font-size: 54px;
    letter-spacing: 0.5px;
    padding-top: 4px;
  }
  .email {
    left: 74px;
    top: 389px;
    width: 543px;
    height: 62px;
    font-size: 29px;
    letter-spacing: -0.8px;
    padding-top: 2px;
  }
  .phone {
    left: 744px;
    top: 389px;
    width: 382px;
    height: 62px;
    font-size: 33px;
    letter-spacing: 9px;
    padding-left: 9px;
    padding-top: 2px;
  }
  .dot-divider {
    position: absolute;
    left: 0;
    top: 332px;
    width: 1200px;
    height: 20px;
  }
  .dot-divider .dot-white { fill: var(--dot-white); }
  .dot-divider .dot-teal { fill: var(--accent-teal); }
</style>
</head>
<body>
<main class="card">
  <div class="card-texture" role="img" aria-label="Dark carbon fibre weave texture"></div>

  <div class="pill website">DHORVATHSTUDIO.EXAMPLE</div>

  <svg class="dot-divider" viewBox="0 0 1200 20" aria-hidden="true">
    <defs>
      <clipPath id="divider-clip"><rect x="75" y="0" width="1047" height="20"/></clipPath>
    </defs>
    <g clip-path="url(#divider-clip)">
      <ellipse class="dot-white" cx="75" cy="10" rx="9" ry="5.8"/>
      <ellipse class="dot-teal" cx="109" cy="10" rx="9" ry="5.8"/>
      <ellipse class="dot-white" cx="143" cy="10" rx="9" ry="5.8"/>
      <ellipse class="dot-teal" cx="176" cy="10" rx="9" ry="5.8"/>
      <ellipse class="dot-white" cx="210" cy="10" rx="9" ry="5.8"/>
      <ellipse class="dot-teal" cx="244" cy="10" rx="9" ry="5.8"/>
      <ellipse class="dot-white" cx="278" cy="10" rx="9" ry="5.8"/>
      <ellipse class="dot-teal" cx="311" cy="10" rx="9" ry="5.8"/>
      <ellipse class="dot-white" cx="345" cy="10" rx="9" ry="5.8"/>
      <ellipse class="dot-teal" cx="379" cy="10" rx="9" ry="5.8"/>
      <ellipse class="dot-white" cx="413" cy="10" rx="9" ry="5.8"/>
      <ellipse class="dot-teal" cx="446" cy="10" rx="9" ry="5.8"/>
      <ellipse class="dot-white" cx="480" cy="10" rx="9" ry="5.8"/>
      <ellipse class="dot-teal" cx="514" cy="10" rx="9" ry="5.8"/>
      <ellipse class="dot-white" cx="548" cy="10" rx="9" ry="5.8"/>
      <ellipse class="dot-teal" cx="582" cy="10" rx="9" ry="5.8"/>
      <ellipse class="dot-white" cx="615" cy="10" rx="9" ry="5.8"/>
      <ellipse class="dot-teal" cx="649" cy="10" rx="9" ry="5.8"/>
      <ellipse class="dot-white" cx="683" cy="10" rx="9" ry="5.8"/>
      <ellipse class="dot-teal" cx="717" cy="10" rx="9" ry="5.8"/>
      <ellipse class="dot-white" cx="750" cy="10" rx="9" ry="5.8"/>
      <ellipse class="dot-teal" cx="784" cy="10" rx="9" ry="5.8"/>
      <ellipse class="dot-white" cx="818" cy="10" rx="9" ry="5.8"/>
      <ellipse class="dot-teal" cx="852" cy="10" rx="9" ry="5.8"/>
      <ellipse class="dot-white" cx="885" cy="10" rx="9" ry="5.8"/>
      <ellipse class="dot-teal" cx="919" cy="10" rx="9" ry="5.8"/>
      <ellipse class="dot-white" cx="953" cy="10" rx="9" ry="5.8"/>
      <ellipse class="dot-teal" cx="987" cy="10" rx="9" ry="5.8"/>
      <ellipse class="dot-white" cx="1020" cy="10" rx="9" ry="5.8"/>
      <ellipse class="dot-teal" cx="1054" cy="10" rx="9" ry="5.8"/>
      <ellipse class="dot-white" cx="1088" cy="10" rx="9" ry="5.8"/>
      <ellipse class="dot-teal" cx="1122" cy="10" rx="9" ry="5.8"/>
    </g>
  </svg>

  <div class="pill email">DAN@DHORVATHSTUDIO.EXAMPLE</div>
  <div class="pill phone">555.418.7260</div>
</main>
</body>
</html>
```